Exercise Physiologist needs business cards

I have a logo, I need business cards (Sole trader) as I am moving to a new location and would like an updated look. I provide gym based exercise rehabilitation, injury prevention and movement assessments. I have over 13 years experience as an Exercise Physiologist. I would like the cards to look professional but not boring and can be a little different to stand out when sitting with other Allied Health Professional cards.

Target Market(s)

GP's, Allied health practitioners, people with injuries wanting to exercise

Industry/Entity Type

Health And Wellness

Contact Information for Business Card

Megan Dorrit - Exercise Physiologist 0437 582 906
14 Larkspur Bend Rd
South Geelong
(Gate 2, Brannock Fitness)
vantorahealth@maildrop-example.com
socialpage-example.com/Vantora

Requirements
Must have
• I would like to include a section to add next appointment date and time space to the back of the card.
Nice to have
• Rounded corners and a black background on 1 or 2 sides.
Should not have
• Pictures of fit/toned bodies etc

```html
<!DOCTYPE html>
<html lang="en">
<head>
<meta charset="utf-8">
<title>Double Sided Business Card – Vantora Health</title>
<link rel="stylesheet" href="https://fonts.googleapis.com/css2?family=Allura&family=Poppins:wght@400;500;800&display=swap">
<style>
  :root {
    --stage: #2b2b2b;
    --royal: #3c62b0;
    --sky: #6aafe0;
    --ink-blue: #2e55a8;
    --paper: #f7f7f8;
    --white: #ffffff;
    --divider: #c8c8cc;
  }
  * { box-sizing: border-box; margin: 0; padding: 0; }
  html, body { width: 1200px; height: 1200px; overflow: hidden; }
  body {
    background: var(--stage);
    font-family: "Poppins", sans-serif;
    position: relative;
  }
  .card {
    position: absolute; left: 285px; width: 630px; height: 360px;
    border-radius: 14px; overflow: hidden;
    box-shadow: 0 14px 30px rgba(0,0,0,.45);
  }
  .card-front { top: 200px; }
  .card-back { top: 640px; }
  .card svg { display: block; }
  .holder-name { font-family: "Allura", cursive; font-size: 56px; fill: var(--white); }
  .holder-role { font-size: 11px; letter-spacing: 4px; fill: var(--white); font-weight: 500; }
  .brand-name { font-size: 30px; font-weight: 500; fill: var(--ink-blue); }
  .brand-tag { font-size: 6.5px; letter-spacing: 1px; fill: var(--ink-blue); }
  .contact-line { font-size: 11.5px; fill: var(--ink-blue); }
  .badge-title { font-size: 18px; font-weight: 800; fill: var(--white); }
  .badge-sub { font-size: 12px; font-weight: 800; letter-spacing: .5px; fill: var(--white); }
  .field-label { font-size: 11px; fill: var(--ink-blue); }
  .notice { font-size: 13px; fill: var(--ink-blue); }
</style>
</head>
<body>
  <section class="card card-front" aria-label="Card front">
    <svg width="630" height="360" viewBox="0 0 630 360">
      <rect width="630" height="360" fill="var(--paper)"/>
      <path d="M0 0 H520 C450 150 250 90 200 220 C180 290 215 340 240 360 H0 Z" fill="var(--royal)"/>
      <path d="M500 0 H520 C450 150 250 90 200 220 C180 290 215 340 240 360 H270 C220 320 205 270 228 215 C275 110 455 160 520 0 Z" fill="var(--white)"/>
      <path d="M510 0 H545 C480 175 285 120 240 225 C220 275 240 330 275 360 H255 C218 325 205 275 228 222 C275 108 470 160 510 0 Z" fill="var(--sky)"/>
      <text class="holder-name" x="40" y="112">Megan Dorrit</text>
      <text class="holder-role" x="46" y="140">EXERCISE PHYSIOLOGIST</text>

      <circle cx="258" cy="252" r="20" fill="none" stroke="var(--ink-blue)" stroke-width="3"/>
      <text class="brand-name" x="284" y="260">vantora</text>
      <text class="brand-tag" x="286" y="273">HEALTH &amp; REHABILITATION</text>

      <line x1="408" y1="190" x2="408" y2="278" stroke="var(--divider)" stroke-width="1.5"/>
      <circle cx="428" cy="200" r="8" fill="var(--sky)"/>
      <rect x="425.5" y="195" width="5" height="10" rx="1.5" fill="var(--white)"/>
      <text class="contact-line" x="443" y="204">0437 582 906</text>
      <circle cx="428" cy="230" r="8" fill="var(--sky)"/>
      <path d="M428 236 L424.5 229.5 A4 4 0 1 1 431.5 229.5 Z" fill="var(--white)"/>
      <text class="contact-line" x="443" y="234">14 Larkspur Bend Rd,</text>
      <text class="contact-line" x="443" y="251">South Geelong</text>
      <text class="contact-line" x="443" y="268">(Gate 2, Brannock Fitness)</text>
    </svg>
  </section>

  <section class="card card-back" aria-label="Card back">
    <svg width="630" height="360" viewBox="0 0 630 360">
      <rect width="630" height="360" fill="var(--paper)"/>
      <path d="M0 0 H630 V70 C500 60 400 70 300 130 C200 185 100 180 0 175 Z" fill="var(--royal)"/>
      <path d="M0 175 C100 180 200 185 300 130 C400 70 500 60 630 70 V85 C500 80 410 95 310 150 C210 205 100 205 0 200 Z" fill="var(--white)"/>
      <path d="M0 185 C100 190 200 192 300 138 C400 82 500 72 630 78 V112 C510 105 420 120 320 175 C220 228 100 225 0 218 Z" fill="var(--sky)"/>

      <circle cx="330" cy="170" r="58" fill="var(--sky)" stroke="var(--white)" stroke-width="5"/>
      <circle cx="330" cy="170" r="64" fill="none" stroke="var(--ink-blue)" stroke-width="4"/>
      <text class="badge-title" x="330" y="166" text-anchor="middle">Your Next</text>
      <text class="badge-sub" x="330" y="186" text-anchor="middle">APPOINTMENT</text>

      <text class="field-label" x="60" y="290">Date :</text>
      <line x1="98" y1="288" x2="340" y2="288" stroke="var(--ink-blue)" stroke-width="1.5"/>
      <text class="field-label" x="360" y="290">Time :</text>
      <line x1="398" y1="288" x2="580" y2="288" stroke="var(--ink-blue)" stroke-width="1.5"/>
      <text class="notice" x="315" y="326" text-anchor="middle">If you are unable to keep your appointment, please contact us as soon as possible.</text>
    </svg>
  </section>
</body>
</html>
```